Microblading website contest - Make it colorful

Beauty salon focusing on microblading need a better website template. Please make a 1 page site mobile optimized and nicer layout with better color formulation. Would love interactive images in the site. You can use stock images and if approve we can pay for it.
Current site:
tessawynkelpeony.com

Inspiration:
https://framqueue.net/shots/41877260-Microblading-HomePage
https://framqueue.net/shots/7914026-Lunetto-Microblading-Eyebrow-Beauty-Salon-Pagewright-Theme

Target Market(s)

women

Industry/Entity Type

beauty salon

Number of Pages Required

1 page

Font styles to use
Serif
Decorative
Script

Requirements
Nice to have
• As pretty as possible

```html
<!DOCTYPE html>
<html lang="en">
<head>
<meta charset="utf-8">
<title>Tessa — Eyebrow Specialist</title>
<link href="https://fonts.googleapis.com/css2?family=Playfair+Display:ital,wght@0,600;0,700;1,600;1,700&family=Lato:wght@400;700&display=swap" rel="stylesheet">
<style>
:root{
  --stage:#e9c3b3;
  --plum:#2b1f2c;
  --plum-2:#3b2a3b;
  --mauve:#9a6b70;
  --mauve-soft:#c89ea0;
  --blush:#f6ece8;
  --blush-2:#efdcd5;
  --ink:#2a2226;
  --muted:#7c6e72;
  --white:#ffffff;
  --star:#d9534f;
  --star-2:#5b5bd6;
}
*{box-sizing:border-box;margin:0;padding:0}
html,body{width:1200px;height:2620px;overflow:hidden}
body{background:var(--stage);font-family:"Lato",Arial,sans-serif;color:var(--ink);position:relative}
.frame{position:absolute;background:var(--white);overflow:hidden;box-shadow:0 6px 24px rgba(80,40,40,.18)}
.desktop{left:60px;top:20px;width:652px;height:2580px}
.mobile-a{left:740px;top:20px;width:190px;height:2580px}
.mobile-b{left:960px;top:20px;width:200px;height:1540px}
.ph{background:linear-gradient(135deg,#e8cfc3,#caa393 60%,#8c6a62)}
.ph.soft{background:linear-gradient(160deg,#f1e2da,#d9b8aa)}
.ph.dark{background:linear-gradient(160deg,#caa393,#6b4c4a)}
h1,h2,h3,.serif{font-family:"Playfair Display",Georgia,serif;font-weight:700}
em{font-style:italic;color:var(--mauve)}
p{font-size:8px;line-height:1.55;color:var(--muted)}
.btn{display:inline-block;background:var(--mauve);color:var(--white);font-size:7px;letter-spacing:1px;text-transform:uppercase;padding:7px 16px;border-radius:2px}
section{position:relative}

/* desktop */
.topbar{height:20px;background:var(--plum);color:#d9c6c8;font-size:6px;display:flex;align-items:center;justify-content:space-between;padding:0 24px}
.dots{display:flex;gap:4px}
.dots i{width:7px;height:7px;border-radius:50%;background:var(--mauve-soft);display:block}
.nav{height:80px;display:flex;align-items:center;justify-content:space-between;padding:0 24px;font-size:7px;letter-spacing:1px;text-transform:uppercase;color:var(--ink)}
.nav ul{list-style:none;display:flex;gap:16px}
.brand{display:flex;flex-direction:column;align-items:center;gap:4px;font-family:"Playfair Display",serif;font-weight:700;font-size:15px;color:var(--plum);text-transform:none;letter-spacing:0}
.brand b{width:10px;height:10px;border-radius:50%;background:var(--mauve);display:block}
.hero{height:260px;background:var(--blush)}
.hero .copy{position:absolute;left:30px;top:60px;width:290px}
.hero h1{font-size:38px;line-height:1.08;color:var(--plum);margin-bottom:18px}
.hero .photo{position:absolute;right:0;top:0;width:320px;height:260px}
.about{height:300px;padding:40px 30px}
.about .photo{position:absolute;left:30px;top:40px;width:200px;height:140px}
.about .copy{position:absolute;left:260px;top:40px;width:340px}
.about h2{font-size:34px;color:var(--plum);margin-bottom:10px}
.about p{margin-bottom:12px}
.why{height:420px;background:var(--plum);color:var(--white)}
.why svg.bg{position:absolute;inset:0}
.why h2{position:absolute;left:30px;top:50px;font-size:32px}
.why h2 em{color:var(--mauve-soft)}
.checks{position:absolute;left:30px;top:120px;list-style:none;display:flex;flex-direction:column;gap:22px;width:200px}
.checks li{font-size:9px;font-weight:700;display:flex;gap:8px;align-items:flex-start}
.checks li span{display:block;font-weight:400;font-size:7px;color:#bfaeb2;margin-top:3px}
.tick{flex:none;width:14px;height:14px;border-radius:50%;background:var(--mauve);display:flex;align-items:center;justify-content:center}
.why .face{position:absolute;left:290px;top:40px;width:240px;height:340px}
.why .btn{position:absolute;left:30px;top:330px}
.services{height:380px;background:var(--blush);text-align:center;padding-top:36px}
.services h2{font-size:32px;color:var(--plum)}
.cards{display:flex;gap:18px;justify-content:center;margin-top:24px}
.card{width:180px;background:var(--white);padding:8px 8px 14px;border:1px solid var(--blush-2)}
.card .ph{height:150px;margin-bottom:10px}
.card h3{font-size:11px;color:var(--plum);margin-bottom:8px}
.feedback{height:460px;background:var(--blush-2);text-align:center;padding-top:40px}
.feedback h2{font-size:32px;color:var(--plum)}
.quotes{display:flex;gap:16px;justify-content:center;margin-top:30px}
.quote{width:180px;background:var(--white);border:1px solid var(--mauve-soft);padding:18px 14px;position:relative}
.quote .mark{font-family:"Playfair Display",serif;font-size:26px;color:var(--mauve);line-height:1;height:16px}
.quote .who{font-size:8px;font-weight:700;color:var(--plum);margin-top:8px}
.pager{display:flex;gap:5px;justify-content:center;margin-top:16px}
.pager i{width:6px;height:6px;border-radius:50%;background:var(--mauve-soft);display:block}
.pager i:first-child{background:var(--mauve)}
.ratings{display:flex;gap:30px;justify-content:center;margin-top:28px}
.rating{display:flex;flex-direction:column;align-items:center;gap:4px}
.rating .name{font-family:"Lato",sans-serif;font-weight:700;font-size:13px;color:var(--plum)}
.stars{display:flex;gap:2px}
.stars i{width:10px;height:10px;background:var(--star);display:block}
.stars.alt i{background:var(--star-2)}
.rating small{font-size:7px;color:var(--muted)}
.gallery{height:360px;text-align:center;padding-top:36px}
.gallery h2{font-size:32px;color:var(--plum)}
.grid{display:grid;grid-template-columns:repeat(5,100px);grid-auto-rows:62px;gap:8px;justify-content:center;margin-top:20px}
.grid .note{background:var(--blush);display:flex;align-items:center;justify-content:center;font-family:"Playfair Display",serif;font-size:11px;color:var(--plum);padding:6px}
.gallery .btn{margin-top:16px}
.footer{height:300px;background:var(--plum);color:#d9c6c8;padding:40px 30px}
.cols{display:flex;gap:40px}
.col h4{font-family:"Playfair Display",serif;color:var(--white);font-size:11px;margin-bottom:10px}
.col ul{list-style:none;font-size:7px;line-height:2.1}
.field{width:180px;height:20px;border:1px solid #6d5766;margin-bottom:8px}
.legal{position:absolute;left:30px;right:30px;bottom:24px;border-top:1px solid #4d3a4a;padding-top:10px;font-size:6px;display:flex;justify-content:space-between}

/* mobile */
.m-nav{height:40px;display:flex;align-items:center;justify-content:space-between;padding:0 12px}
.m-nav .brand{font-size:10px;flex-direction:row;gap:4px}
.m-nav .brand b{width:6px;height:6px}
.burger{width:14px;height:9px;border-top:2px solid var(--plum);border-bottom:2px solid var(--plum);position:relative}
.burger:after{content:"";position:absolute;left:0;right:0;top:1.5px;border-top:2px solid var(--plum)}
.m-hero{height:280px;background:var(--blush)}
.m-hero h1{position:absolute;left:12px;top:20px;font-size:20px;line-height:1.1;color:var(--plum);width:110px;z-index:1}
.m-hero .photo{position:absolute;right:0;top:0;width:110px;height:200px}
.m-hero .btn{position:absolute;left:12px;top:220px}
.m-about{height:440px;padding:20px 12px}
.m-about .ph{height:130px;margin-bottom:14px}
.m-about h2{font-size:22px;color:var(--plum);margin-bottom:8px}
.m-about p{font-size:7px;margin-bottom:12px}
.m-why{height:660px;background:var(--plum);color:var(--white);text-align:center;padding-top:24px}
.m-why h2{font-size:20px}
.m-why h2 em{color:var(--mauve-soft)}
.m-why .checks{position:static;margin:20px auto 0;width:150px;text-align:left;gap:26px}
.m-why .face{width:150px;height:200px;margin:26px auto 0}
.m-why .btn{margin-top:20px}
.m-services{height:1160px;background:var(--blush);text-align:center;padding-top:26px}
.m-services h2{font-size:20px;color:var(--plum)}
.m-card{margin:18px 14px 0;background:var(--white);padding:8px 8px 14px}
.m-card .ph{height:200px;margin-bottom:10px}
.m-card h3{font-size:10px;color:var(--plum);margin-bottom:8px}
.m-feedback{height:280px;background:var(--blush-2);text-align:center;padding-top:22px}
.m-feedback h2{font-size:20px;color:var(--plum);line-height:1.1}
.m-feedback .quote{width:170px;margin:18px auto 0;text-align:center}
.m-ratings{height:200px;background:var(--blush-2);display:flex;flex-direction:column;align-items:center;gap:26px;padding-top:20px}
.m-gallery{height:240px;text-align:center;padding-top:22px}
.m-gallery h2{font-size:20px;color:var(--plum)}
.m-gallery .pair{display:flex;gap:6px;justify-content:center;margin-top:16px}
.m-gallery .pair .ph{width:84px;height:110px}
.m-footer{height:820px;background:var(--plum);color:#d9c6c8;padding:30px 18px;text-align:center}
.m-footer .col{margin-bottom:40px}
.m-footer .field{width:150px;margin:0 auto 8px}
.m-footer .dots{justify-content:center;gap:8px}
.m-footer .dots i{width:14px;height:14px}
</style>
</head>
<body>

<!-- Desktop layout -->
<main class="frame desktop">
  <div class="topbar"><span>+1 (555) 014-2288 · hello@tessawynkelpeony.com</span><div class="dots"><i></i><i></i><i></i></div></div>
  <header class="nav">
    <ul><li>Home</li><li>About</li><li>Services</li><li>Gallery</li></ul>
    <div class="brand"><b></b>Tessa</div>
    <ul><li>Feedback</li><li>Contact</li><li>+1 (555) 014-2288</li></ul>
  </header>

  <section class="hero">
    <div class="copy">
      <h1>Your Personal <em>Eyebrow</em> Specialist</h1>
      <span class="btn">Book Now</span>
    </div>
    <div class="photo ph soft" role="img" aria-label="Portrait of a client with shaped natural brows"></div>
  </section>

  <section class="about">
    <div class="photo ph dark" role="img" aria-label="Artist performing a microblading treatment"></div>
    <div class="copy">
      <h2>About <em>Tessa</em></h2>
      <p>Certified brow artist with a calm studio, gentle hands and an eye for balance. Every treatment starts with mapping your face so the result looks like your own brows, only better.</p>
      <p>From first consultation to final touch-up, you are guided through each step with care and honest advice.</p>
      <span class="btn">Read More</span>
    </div>
  </section>

  <section class="why">
    <svg class="bg" width="652" height="420" viewBox="0 0 652 420" aria-hidden="true">
      <polygon points="0,0 652,0 652,60 0,120" fill="#3b2a3b"/>
      <polygon points="0,420 652,420 652,300 0,380" fill="#3b2a3b"/>
      <line x1="560" y1="40" x2="620" y2="380" stroke="#9a6b70" stroke-width="1"/>
    </svg>
    <h2>Why <em>Tessa</em></h2>
    <ul class="checks">
      <li><i class="tick"><svg width="8" height="8" viewBox="0 0 8 8"><path d="M1 4l2 2 4-4" stroke="#fff" stroke-width="1.4" fill="none"/></svg></i><div>Licensed Microblading Artist<span>Fully certified and insured studio.</span></div></li>
      <li><i class="tick"><svg width="8" height="8" viewBox="0 0 8 8"><path d="M1 4l2 2 4-4" stroke="#fff" stroke-width="1.4" fill="none"/></svg></i><div>Years of Experience<span>Hundreds of happy returning clients.</span></div></li>
      <li><i class="tick"><svg width="8" height="8" viewBox="0 0 8 8"><path d="M1 4l2 2 4-4" stroke="#fff" stroke-width="1.4" fill="none"/></svg></i><div>European Latest Technique<span>Modern tools for soft, lasting results.</span></div></li>
    </ul>
    <div class="face ph" role="img" aria-label="Before and after brow treatment portrait"></div>
    <span class="btn">Book Now</span>
  </section>

  <section class="services">
    <h2>Our <em>Services</em></h2>
    <div class="cards">
      <div class="card"><div class="ph" role="img" aria-label="Close-up of natural microbladed brows"></div><h3>Natural Brows</h3><span class="btn">Learn More</span></div>
      <div class="card"><div class="ph soft" role="img" aria-label="Close-up of powder brows"></div><h3>Powder Eyebrow<br>(Natural Eyeshadow)</h3><span class="btn">Learn More</span></div>
      <div class="card"><div class="ph dark" role="img" aria-label="Scalp micropigmentation result"></div><h3>Scalp Micropigmentation</h3><span class="btn">Learn More</span></div>
    </div>
  </section>

  <section class="feedback">
    <h2>Customer’s <em>Feedback</em></h2>
    <div class="quotes">
      <div class="quote"><div class="mark">“</div><p>My brows finally look full and natural. The whole visit felt relaxed and I loved the result.</p><div class="who">Anna M.</div></div>
      <div class="quote"><div class="mark">“</div><p>Careful, patient and so talented. I wake up every morning with perfect brows now.</p><div class="who">Clara R.</div></div>
      <div class="quote"><div class="mark">“</div><p>Best decision I made this year. Soft, even shape and healing went smoothly.</p><div class="who">Jodie K.</div></div>
    </div>
    <div class="pager"><i></i><i></i><i></i></div>
    <div class="ratings">
      <div class="rating"><span class="name">Ratewell</span><div class="stars"><i></i><i></i><i></i><i></i><i></i></div><small>25 Reviews</small></div>
      <div class="rating"><span class="name">Nookbook</span><div class="stars alt"><i></i><i></i><i></i><i></i><i></i></div><small>25 Reviews</small></div>
    </div>
  </section>

  <section class="gallery">
    <h2>Tessa’s <em>Gallery</em></h2>
    <div class="grid">
      <div class="ph" role="img" aria-label="Brow result photo"></div>
      <div class="ph soft" role="img" aria-label="Brow result photo"></div>
      <div class="ph dark" role="img" aria-label="Brow result photo"></div>
      <div class="ph" role="img" aria-label="Brow result photo"></div>
      <div class="ph soft" role="img" aria-label="Brow result photo"></div>
      <div class="ph dark" role="img" aria-label="Brow result photo"></div>
      <div class="ph" role="img" aria-label="Brow result photo"></div>
      <div class="note">Real Clients, Real Results</div>
      <div class="ph soft" role="img" aria-label="Brow result photo"></div>
      <div class="ph dark" role="img" aria-label="Brow result photo"></div>
      <div class="ph soft" role="img" aria-label="Brow result photo"></div>
      <div class="ph" role="img" aria-label="Brow result photo"></div>
      <div class="ph dark" role="img" aria-label="Brow result photo"></div>
      <div class="ph soft" role="img" aria-label="Brow result photo"></div>
      <div class="ph" role="img" aria-label="Brow result photo"></div>
    </div>
    <span class="btn">View More</span>
  </section>

  <footer class="footer">
    <div class="cols">
      <div class="col"><h4>Quick Links</h4><ul><li>Home</li><li>About</li><li>Services</li><li>Gallery</li><li>Contact</li></ul></div>
      <div class="col"><h4>Contact Us</h4><ul><li>+1 (555) 014-2288</li><li>hello@tessawynkelpeony.com</li><li>48 Rowan Lane, Suite 3</li><li>Mon – Sat, 9am – 6pm</li></ul></div>
      <div class="col"><h4>Join Our Newsletter</h4><div class="field"></div><span class="btn">Subscribe</span></div>
      <div class="col"><h4>Follow</h4><div class="dots"><i></i><i></i><i></i><i></i></div></div>
    </div>
    <div class="legal"><span>© 2024 Tessa Brow Studio. All rights reserved.</span><span>tessawynkelpeony.com</span></div>
  </footer>
</main>

<!-- Mobile layout, first column -->
<main class="frame mobile-a">
  <header class="m-nav"><div class="brand"><b></b>Tessa</div><div class="burger"></div></header>
  <section class="m-hero">
    <h1>Your Personal <em>Eyebrow</em> Specialist</h1>
    <div class="photo ph soft" role="img" aria-label="Portrait of a client with shaped natural brows"></div>
    <span class="btn">Book Now</span>
  </section>
  <section class="m-about">
    <div class="ph dark" role="img" aria-label="Artist performing a microblading treatment"></div>
    <h2>About <em>Tessa</em></h2>
    <p>Certified brow artist with a calm studio and an eye for balance. Every treatment starts with careful mapping of your face.</p>
    <span class="btn">Read More</span>
  </section>
  <section class="m-why">
    <h2>Why <em>Tessa</em></h2>
    <ul class="checks">
      <li><i class="tick"><svg width="8" height="8" viewBox="0 0 8 8"><path d="M1 4l2 2 4-4" stroke="#fff" stroke-width="1.4" fill="none"/></svg></i><div>Licensed Microblading Artist</div></li>
      <li><i class="tick"><svg width="8" height="8" viewBox="0 0 8 8"><path d="M1 4l2 2 4-4" stroke="#fff" stroke-width="1.4" fill="none"/></svg></i><div>Years of Experience</div></li>
      <li><i class="tick"><svg width="8" height="8" viewBox="0 0 8 8"><path d="M1 4l2 2 4-4" stroke="#fff" stroke-width="1.4" fill="none"/></svg></i><div>European Latest Technique</div></li>
    </ul>
    <div class="face ph" role="img" aria-label="Before and after brow treatment portrait"></div>
    <span class="btn">Book Now</span>
  </section>
  <section class="m-services">
    <h2>Our <em>Services</em></h2>
    <div class="m-card"><div class="ph" role="img" aria-label="Close-up of natural microbladed brows"></div><h3>Natural Brows</h3><span class="btn">Learn More</span></div>
    <div class="m-card"><div class="ph soft" role="img" aria-label="Close-up of powder brows"></div><h3>Powder Eyebrow<br>(Natural Eyeshadow)</h3><span class="btn">Learn More</span></div>
    <div class="m-card"><div class="ph dark" role="img" aria-label="Scalp micropigmentation result"></div><h3>Scalp Micropigmentation</h3><span class="btn">Learn More</span></div>
  </section>
</main>

<!-- Mobile layout, second column -->
<main class="frame mobile-b">
  <section class="m-feedback">
    <h2>Customer’s<br><em>Feedback</em></h2>
    <div class="quote"><div class="mark">“</div><p>My brows finally look full and natural. The whole visit felt relaxed and I loved the result.</p><div class="who">Anna M.</div></div>
    <div class="pager"><i></i><i></i><i></i></div>
  </section>
  <section class="m-ratings">
    <div class="rating"><span class="name">Ratewell</span><div class="stars"><i></i><i></i><i></i><i></i><i></i></div><small>25 Reviews</small></div>
    <div class="rating"><span class="name">Nookbook</span><div class="stars alt"><i></i><i></i><i></i><i></i><i></i></div><small>25 Reviews</small></div>
  </section>
  <section class="m-gallery">
    <h2>Tessa’s <em>Gallery</em></h2>
    <div class="pair">
      <div class="ph soft" role="img" aria-label="Brow result photo"></div>
      <div class="ph" role="img" aria-label="Brow result photo"></div>
    </div>
  </section>
  <footer class="m-footer">
    <div class="col"><h4>Quick Links</h4><ul><li>Home</li><li>About</li><li>Services</li><li>Gallery</li><li>Contact</li></ul></div>
    <div class="col"><h4>Contact Us</h4><ul><li>+1 (555) 014-2288</li><li>hello@tessawynkelpeony.com</li><li>48 Rowan Lane, Suite 3</li></ul></div>
    <div class="col"><h4>Join Our Newsletter</h4><div class="field"></div><span class="btn">Subscribe</span></div>
    <div class="dots"><i></i><i></i><i></i><i></i></div>
  </footer>
</main>

</body>
</html>
```